Women's Online Clothing Boutique Needs Business Cards

I already have a logo that I would like to use. Some of the things that interest me is black business cards, foil embossed logo, glossy embossed logo, leopard print, no yellow font, rounded edges. I even like just a large logo on the front side with all of my information on the back side.

Contact Information for Business Card

https://silverheron.shopvenlo.com/
https://www.pagelink.net/thesilverheronboutique/
https://www.picfeed.net/thesilverheronboutique/
silverheronboutique@mailora.net

Requirements
Must have
• My Logo
Nice to have
• Leopard Print
Should not have
• No Yellow Font

```html
<!DOCTYPE html>
<html lang="en">
<head>
<meta charset="utf-8">
<title>The Silver Heron Boutique – Business Card</title>
<link rel="stylesheet" href="https://fonts.googleapis.com/css2?family=Asap:wght@400;500;700&display=swap">
<style>
  :root {
    --board: #e6e6e6;
    --label: #6a6a6a;
    --card-black: #1a1c1e;
    --card-white: #ffffff;
    --print-magenta: #8e1464;
    --print-deep: #3a1430;
    --swatch-varnish: #ff00a8;
    --swatch-gold: #e0b800;
    --swatch-black: #1c1c1c;
    --gold-light: #d9aa06;
    --gold-dark: #8a4206;
    --ink: #1e1e1e;
    --logo-white: #ffffff;
  }
  * { margin: 0; padding: 0; box-sizing: border-box; }
  html, body { width: 1200px; height: 780px; overflow: hidden; }
  body {
    position: relative;
    background: var(--board);
    font-family: "Asap", Arial, sans-serif;
  }

  .legend-item {
    position: absolute;
    display: flex;
    align-items: center;
    gap: 10px;
    font-weight: 700;
    font-size: 14px;
    color: var(--label);
    white-space: nowrap;
  }
  .swatch {
    width: 24px; height: 24px;
    border-radius: 5px;
    flex: none;
  }
  .swatch--varnish { background: var(--swatch-varnish); }
  .swatch--gold { background: var(--swatch-gold); }
  .swatch--black { background: var(--swatch-black); }

  .card {
    position: absolute;
    top: 192px;
    width: 252px;
    height: 399px;
    overflow: hidden;
  }
  .card--front { left: 316px; background: var(--card-black); }
  .card--back { left: 641px; background: var(--card-white); }

  .print-band {
    position: absolute;
    left: 0; width: 100%; height: 121px;
    background: linear-gradient(150deg,
      var(--print-magenta) 0%,
      var(--print-deep) 30%,
      var(--print-magenta) 55%,
      var(--print-deep) 80%,
      var(--print-magenta) 100%);
  }
  .print-band--top { top: 0; }
  .print-band--bottom { bottom: 0; }

  .brand-name,
  .brand-sub {
    position: absolute;
    left: 0; right: 0;
    text-align: center;
    color: var(--logo-white);
    font-weight: 500;
    white-space: nowrap;
  }
  .brand-name { top: 190px; font-size: 26px; line-height: 30px; }
  .brand-sub { top: 222px; font-size: 22px; line-height: 26px; }
  .brand-rule {
    position: absolute;
    top: 235px;
    height: 1px;
    width: 56px;
    background: var(--logo-white);
  }
  .brand-rule--left { left: 19px; }
  .brand-rule--right { right: 19px; }

  .holder-name {
    position: absolute;
    left: 26px; top: 24px;
    color: var(--ink);
    font-size: 28px;
    font-weight: 400;
    line-height: 31px;
  }
  .holder-name strong { display: block; font-weight: 700; }

  .mascot-art {
    position: absolute;
    left: 0; top: 130px;
    width: 100%; height: 155px;
    background: linear-gradient(225deg, var(--gold-light) 0%, #c08a04 50%, var(--gold-dark) 100%);
  }

  .contact {
    position: absolute;
    left: 17px; top: 306px;
    list-style: none;
    color: var(--ink);
    font-size: 14px;
    line-height: 23px;
  }
  .contact li:first-child, .contact li:nth-child(2) { padding-left: 2px; }
</style>
</head>
<body>

  <div class="legend-item" style="left:331px; top:156px;">
    <span class="swatch swatch--varnish"></span>Varnish UV (glossy embossed)
  </div>

  <section class="card card--front">
    <div class="print-band print-band--top" role="img" aria-label="Leopard print of magenta spots on black, in glossy UV varnish"></div>
    <p class="brand-name">The Silver Heron</p>
    <span class="brand-rule brand-rule--left"></span>
    <p class="brand-sub">Boutique</p>
    <span class="brand-rule brand-rule--right"></span>
    <div class="print-band print-band--bottom" role="img" aria-label="Leopard print of magenta spots on black, in glossy UV varnish"></div>
  </section>

  <section class="card card--back">
    <h1 class="holder-name">Clara<strong>Whitfield</strong></h1>
    <div class="mascot-art" role="img" aria-label="Gold foil illustration of a big cat resting on a line"></div>
    <ul class="contact">
      <li>+00 555-014-2288</li>
      <li>+00 555-014-2288</li>
      <li>silverheronboutique@mailora.net</li>
    </ul>
  </section>

  <div class="legend-item" style="left:941px; top:194px;">
    <span class="swatch swatch--gold"></span>Gold
  </div>
  <div class="legend-item" style="left:941px; top:224px;">
    <span class="swatch swatch--varnish"></span>Varnish UV (glossy embossed)
  </div>
  <div class="legend-item" style="left:941px; top:255px;">
    <span class="swatch swatch--black"></span>Black
  </div>

</body>
</html>
```